New Business Card Design Project

Vorin focus is ZVR Asset Management and Supply Chain.
We have Business Process Experts that can help you get the maximum potential out of your KLM T/7ORBA ERP. We look to understand your business and through the People, Process and Technologies to make you streamline your users digital experience.

The back of the card will be either;
- all black with the orange logo
- all orange with the black logo
- all white with the orange logo
- or make something special
The detail side, show me your best designs.
Try having the side a different colour. So if the one side is black the other is white…

Target Market(s)

Corporate Professional Business

Industry/Entity Type

Mining, Software

Contact Information for Business Card

Name, Position, brief what we do

Colors
F0912C
F2A743
F7CA91
FBE8D2
FDF5EE

Requirements
Must have
• Real Simple Solutions to Big Problems

```html
<!DOCTYPE html>
<html lang="en">
<head>
<meta charset="utf-8">
<title>Vorin Business Card</title>
<link href="https://fonts.googleapis.com/css2?family=Lato:wght@300;400;700;900&display=swap" rel="stylesheet">
<style>
  :root {
    --stage: #2a2a2a;
    --card: #1e1e1e;
    --orange: #f37721;
    --white: #f2f2f2;
    --muted: #d9d9d9;
  }
  * { margin: 0; padding: 0; box-sizing: border-box; }
  html, body {
    width: 1200px; height: 875px; overflow: hidden;
    background: var(--stage);
    font-family: "Lato", sans-serif;
  }
  .stage {
    position: relative; width: 1200px; height: 875px;
    display: flex; align-items: center; justify-content: space-between;
    padding: 0 40px;
  }
  .card {
    width: 540px; height: 309px;
    background: var(--card);
    border-radius: 18px;
    box-shadow: 0 20px 40px rgba(0,0,0,.45);
    position: relative;
    overflow: hidden;
  }
  .brand {
    display: flex; align-items: center; gap: 12px;
    color: var(--orange); font-weight: 900; white-space: nowrap;
  }
  .brand-dot { flex: none; border-radius: 50%; background: var(--orange); }

  .card-back {
    display: flex; flex-direction: column; align-items: center; justify-content: center;
  }
  .card-back .brand { font-size: 64px; }
  .card-back .brand-dot { width: 40px; height: 40px; }
  .tagline {
    margin-top: 40px; color: var(--white);
    font-size: 15px; font-weight: 400; letter-spacing: .3px;
  }

  .card-front { display: flex; align-items: center; }
  .front-mark {
    width: 205px; display: flex; justify-content: center;
  }
  .front-mark .brand { font-size: 40px; gap: 9px; }
  .front-mark .brand-dot { width: 26px; height: 26px; }
  .divider {
    flex: none; width: 1.5px; height: 190px; background: var(--orange);
  }
  .details { padding-left: 26px; padding-right: 20px; color: var(--white); }
  .person-name {
    color: var(--orange); font-weight: 900; font-size: 30px;
    letter-spacing: .5px; text-transform: uppercase; line-height: 1;
  }
  .person-role { font-weight: 300; font-size: 15px; margin-top: 4px; }
  .contact-list { list-style: none; margin-top: 14px; }
  .contact-item {
    display: flex; align-items: flex-start; gap: 9px;
    font-size: 12.5px; line-height: 1.45; color: var(--muted);
  }
  .contact-item + .contact-item { margin-top: 3px; }
  .contact-item svg { flex: none; width: 11px; height: 11px; margin-top: 3px; fill: var(--orange); }
  .company { font-weight: 700; color: var(--white); }
  .address-block { margin-bottom: 6px; }
</style>
</head>
<body>
<main class="stage">
  <section class="card card-back">
    <div class="brand"><span class="brand-dot"></span><span>Vorin</span></div>
    <p class="tagline">Real Simple Solutions to Big Problems</p>
  </section>

  <section class="card card-front">
    <div class="front-mark">
      <div class="brand"><span class="brand-dot"></span><span>Vorin</span></div>
    </div>
    <div class="divider"></div>
    <div class="details">
      <h1 class="person-name">Marcus Hale</h1>
      <p class="person-role">Founder &amp; CEO</p>
      <ul class="contact-list">
        <li class="contact-item address-block">
          <svg viewBox="0 0 12 12"><path d="M6 0a4 4 0 0 0-4 4c0 3 4 8 4 8s4-5 4-8a4 4 0 0 0-4-4zm0 5.6A1.6 1.6 0 1 1 6 2.4a1.6 1.6 0 0 1 0 3.2z"/></svg>
          <span><span class="company">ZVR Asset Management &amp; Supply Chain.</span><br>Street Address Here, City<br>State, Country, ZIP 123</span>
        </li>
        <li class="contact-item">
          <svg viewBox="0 0 12 12"><path d="M2.4 0.6l2 2-1 1.4a7 7 0 0 0 4.6 4.6l1.4-1 2 2-1.4 1.8C5 11 1 7 .6 2z"/></svg>
          <span>(555) 014-2270</span>
        </li>
        <li class="contact-item">
          <svg viewBox="0 0 12 12"><path d="M3 0h6a1 1 0 0 1 1 1v10a1 1 0 0 1-1 1H3a1 1 0 0 1-1-1V1a1 1 0 0 1 1-1zm0 1.5v8h6v-8z"/></svg>
          <span>(555) 014-2270</span>
        </li>
        <li class="contact-item">
          <svg viewBox="0 0 12 12"><path d="M0 2h12v8H0zm1.2 1L6 6.4 10.8 3z"/></svg>
          <span>info@vorinerp.com</span>
        </li>
        <li class="contact-item">
          <svg viewBox="0 0 12 12"><path d="M6 0a6 6 0 1 0 0 12A6 6 0 0 0 6 0zm0 1.2a4.8 4.8 0 0 1 0 9.6 4.8 4.8 0 0 1 0-9.6zM3 5.4h6v1.2H3z"/></svg>
          <span>vorinerp.com</span>
        </li>
      </ul>
    </div>
  </section>
</main>
</body>
</html>
```